Hello my name is Colin, I am Starting a business called Harbor Health and fitness and am in need of a memorable business card.
It is a personal training studio. I have added the logo that i would like to be on the left center om my business card. i would like room left up the top for a heading sentence such as. "Is your body shocking for all the wrong reasons". there must be room left on the right of the logo below the main heading for 3 sub headings.
then under those 3 headings and logo room for another larger heading eg. "give me a call and learn how to eat chocolate, drink bear and have great sex". in what room is left i would like to be used for my contact details, use I'm Colin Pettersby your fitness expert on the left then on the right Phone, Email and website space in at least 12 Point. Very specific i know :) now onto the back, for the back i would like an eye catching graphic and room for one main headline and 3 bullet points centered just write anything i will choose what to put in them when i pick a winner. Thank you very much for sticking through all of that :) i appreciate you taking the time to read it and hopefully undergo designing me a business card.
I can't wait to see the designs!

Target Market(s)

slightly more towards females although it would probably be best if it was targeted towards both sexes

Industry/Entity Type

Training

Requirements
Nice to have
• I would love to see if anyone could come up with a design that would really make my card stand out and be memorable.
Should not have
• tacky fitness photos of abs and muscles etc.

```html
<!DOCTYPE html>
<html lang="en">
<head>
<meta charset="utf-8">
<title>Harbor Health and Fitness – Business Card</title>
<link rel="stylesheet" href="https://fonts.googleapis.com/css2?family=Jost:wght@300;400;800&display=swap">
<style>
  :root {
    --card-grey: #c0c0c0;
    --card-blue: #0a46b8;
    --brand-magenta: #a31a6b;
    --brand-navy: #1c4a8a;
    --faint-pink: #d8abc6;
    --faint-plum: #c25f9c;
    --soft-text: #c9cbd8;
    --white: #ffffff;
    --edge: #8a8a8a;
  }
  * { margin: 0; padding: 0; box-sizing: border-box; }
  html, body {
    width: 1007px; height: 1200px; overflow: hidden; background: var(--white);
    font-family: "Jost", "Futura", sans-serif;
  }
  .card {
    position: absolute; left: 0; width: 1007px; height: 577px;
    border: 1px solid var(--edge); overflow: hidden;
  }
  .card--front { top: 0; background: var(--card-grey); }
  .card--back { top: 623px; background: var(--card-blue); }
  .card__waves { position: absolute; inset: 0; width: 100%; height: 100%; }
  .wave--magenta { fill: var(--brand-magenta); }
  .wave--blue { fill: var(--card-blue); }
  .wave--grey { fill: var(--card-grey); }

  .strong { font-weight: 800; }

  .headline {
    position: absolute; left: 40px; top: 38px;
    color: var(--brand-magenta); font-weight: 300; font-size: 32px; line-height: 40px;
  }
  .pitch {
    position: absolute; right: 25px; top: 38px; text-align: right;
    color: var(--brand-magenta); font-weight: 300; font-size: 32px; line-height: 40.5px;
  }
  .brand-name {
    position: absolute; left: 40px; top: 128px;
    color: var(--brand-navy); font-weight: 400; font-size: 46px; line-height: 46px;
  }
  .brand-name small { display: block; font-size: 46px; }
  .brand-mark-faint {
    position: absolute; font-weight: 400; line-height: 1;
  }
  .brand-mark-faint--front { left: 548px; top: 278px; color: var(--faint-pink); font-size: 62px; }
  .brand-mark-faint--back { left: 78px; top: 408px; color: var(--faint-plum); font-size: 58px; }

  .trainer {
    position: absolute; left: 24px; top: 398px; color: var(--white);
  }
  .trainer__name { font-weight: 800; font-size: 38px; line-height: 44px; }
  .trainer__role { font-weight: 300; font-size: 23px; line-height: 26px; }

  .contact {
    position: absolute; bottom: 10px; color: var(--white);
    font-weight: 400; font-size: 13.5px;
  }
  .contact--phone { left: 24px; }
  .contact--web { right: 24px; }

  .points {
    position: absolute; right: 44px; top: 84px; list-style: none; text-align: right;
    color: var(--soft-text); font-weight: 400; font-size: 20px;
  }
  .points li { height: 64px; line-height: 30px; }
</style>
</head>
<body>

<section class="card card--front">
  <svg class="card__waves" viewBox="0 0 1007 577" preserveAspectRatio="none" aria-hidden="true">
    <path class="wave--magenta" d="M300,356 C470,335 560,375 640,425 C760,495 870,455 1007,440 L1007,577 L0,577 Z"/>
    <path class="wave--blue" d="M0,392 C150,362 300,344 420,362 C560,385 640,480 760,505 C860,525 950,520 1007,512 L1007,577 L0,577 Z"/>
  </svg>

  <p class="headline">Is your body <span class="strong">shocking</span><br>for all the wrong <span class="strong">reasons</span></p>

  <p class="brand-name">Harbor<small>Health and Fitness</small></p>

  <p class="pitch">give me a call<br>and learn how to<br>eat <span class="strong">chocolate</span><br><span class="strong">drink bear</span> and<br>have <span class="strong">great sex</span></p>

  <p class="brand-mark-faint brand-mark-faint--front">Harbor<br>Health and Fitness</p>

  <div class="trainer">
    <p class="trainer__name">Colin Pettersby</p>
    <p class="trainer__role">your fitness expert</p>
  </div>

  <p class="contact contact--phone">phone: 0-000-0-000-0000</p>
  <p class="contact contact--web">email: colinpettersby@harborfit.com &nbsp;•&nbsp; www.harborfit.com</p>
</section>

<section class="card card--back">
  <svg class="card__waves" viewBox="0 0 1007 577" preserveAspectRatio="none" aria-hidden="true">
    <path class="wave--grey" d="M0,392 C200,330 420,300 600,345 C780,390 900,420 1007,418 L1007,577 L0,577 Z"/>
    <path class="wave--magenta" d="M0,392 C180,350 360,330 520,360 C700,395 850,470 1007,477 L1007,577 L0,577 Z"/>
  </svg>

  <ul class="points">
    <li>Is your body <span class="strong">shocking</span> for all the wrong <span class="strong">reasons</span></li>
    <li>Is your body <span class="strong">shocking</span> for all the wrong <span class="strong">reasons</span></li>
    <li>Is your body <span class="strong">shocking</span> for all the wrong <span class="strong">reasons</span></li>
    <li>Is your body <span class="strong">shocking</span> for all the wrong <span class="strong">reasons</span></li>
  </ul>

  <p class="brand-mark-faint brand-mark-faint--back">Harbor<br>Health and Fitness</p>
</section>

</body>
</html>
```